Sunwellflow Aquadeepflow Depot

Need a brochure to send to new prospective clients, giving them an idea of what we are and what we can do for them.
To be sent as an attachment to an email.
Printable if possible to hand out at Pastoral Expo Week.
http://www.sunwellflow.com.au/
http://www.aquadeepflow.com.au/
http://www.wellflowy.net.au/
All three of these site are part of what I do.

Target Market(s)

Rural, Sheep and cattle stations, water bore users, out of city living.

Colors
0255a3
0692cd

Requirements
Must have
• Print and email version

```html
<!DOCTYPE html>
<html lang="en">
<head>
<meta charset="utf-8">
<title>Sunwellflow Brochure Spread</title>
<link href="https://fonts.googleapis.com/css2?family=Didact+Gothic&family=Roboto+Condensed:ital,wght@1,700&display=swap" rel="stylesheet">
<style>
  :root{
    --blue-deep:#0255a3;
    --blue:#0692cd;
    --grey:#75797e;
    --ink:#3a3f47;
    --paper:#fbfcfd;
    --backdrop:#dde8ed;
  }
  *{box-sizing:border-box;margin:0;padding:0}
  html,body{width:1200px;height:789px;overflow:hidden;background:var(--backdrop)}
  body{font-family:"Didact Gothic",sans-serif;color:var(--ink)}
  .spread{position:absolute;left:70px;top:20px;width:1060px;height:750px;display:flex;box-shadow:0 6px 18px rgba(0,0,0,.15)}
  .page{position:relative;width:530px;height:750px;background:var(--paper);overflow:hidden}
  .page--left{border-right:1px solid #e2e6ea}
  .header-bar{position:absolute;left:0;top:28px;width:530px;height:40px}
  .header-title{position:absolute;left:28px;top:31px;color:#fff;font-size:15px;letter-spacing:.3px;font-weight:400}
  .copy{font-size:8px;line-height:1.35}
  .copy p{margin-bottom:5px}
  .left-column{position:absolute;left:40px;top:80px;width:450px}
  .section-heading{font-size:18px;line-height:1.2;color:var(--blue);font-weight:400;margin-top:6px}
  .section-sub{font-size:12px;line-height:1.25;color:var(--ink);margin:2px 0 6px}
  .copy strong{font-weight:700;color:#1d2229}
  .media{position:absolute}
  .media--diagram{left:40px;top:384px;width:240px;height:232px;background:linear-gradient(160deg,#ffffff,#e9eef3)}
  .media--truck{left:292px;top:384px;width:200px;height:112px;background:linear-gradient(180deg,#a9c4dc 0%,#c9b892 55%,#7c6a4d 100%)}
  .media--bore{left:292px;top:502px;width:97px;height:114px;background:linear-gradient(180deg,#7a9a5e,#a08a68)}
  .media--controller-small{left:395px;top:502px;width:97px;height:114px;background:linear-gradient(180deg,#6f9456,#c9d0d4 60%,#8aa36d)}
  .services{position:absolute;left:40px;top:82px;list-style:none;font-size:13.5px;line-height:1.55}
  .services li{display:flex;align-items:center;gap:7px}
  .services svg{width:11px;height:11px;flex:none}
  .media--shelves{left:408px;top:96px;width:92px;height:140px;background:linear-gradient(180deg,#c8cfd6,#7e8a96 60%,#b8742f)}
  .media--controller{left:40px;top:250px;width:232px;height:260px;background:linear-gradient(180deg,#d9dde0 0%,#9aa3a8 45%,#b3532a 100%)}
  .media--panel{left:278px;top:250px;width:222px;height:126px;background:linear-gradient(180deg,#b7cfe6 0%,#5b7a96 45%,#7e8f5a 100%)}
  .media--drilling{left:278px;top:382px;width:222px;height:128px;background:linear-gradient(180deg,#bcd3e6 0%,#6f8f4f 50%,#b4562c 100%)}
  .owner-copy{position:absolute;left:40px;top:520px;width:460px}
  .owner-copy .lead{color:var(--blue)}
  .footer{position:absolute;left:0;bottom:0;width:530px;height:110px}
  .footer svg{position:absolute;left:0;top:0}
  .call-line{position:absolute;top:24px;font-family:"Roboto Condensed",sans-serif;font-style:italic;font-weight:700;font-size:17px;color:#1d2229;letter-spacing:.2px}
  .web-links{position:absolute;bottom:14px;color:#fff;font-size:10.5px;display:flex;gap:10px}
  .web-links span+span::before{content:"|";margin-right:10px;opacity:.8}
  .page--left .call-line{left:40px}
  .page--left .web-links{left:40px}
  .page--right .call-line{right:40px;top:46px}
  .page--right .web-links{right:40px}
</style>
</head>
<body>
<main class="spread">
  <section class="page page--left">
    <svg class="header-bar" viewBox="0 0 530 40">
      <polygon points="268,6 530,6 530,40 292,40" fill="var(--grey)"/>
      <polygon points="0,0 262,0 286,26 0,26" fill="var(--blue-deep)"/>
      <polygon points="0,0 262,0 272,11 0,11" fill="var(--blue)" opacity=".45"/>
    </svg>
    <h1 class="header-title">Introduction</h1>

    <div class="left-column">
      <div class="copy">
        <p>If you are looking to pump water from a water bore with mains power or pump water from a bore, creek or dam with solar power we are the experts. Aquadeepflow Depot and Sunwellflow has grown from my water bore drilling, pump service and installation business, servicing local clients - into an Australia wide online based business servicing over a thousand clients, with the same enthusiasm as looking after my mates down the road.</p>
        <p>We offer the best pumps and pumping equipment available from throughout the world, sourced locally from our suppliers in Australia. The range includes Torrentek, Helioflo, Ridgeway Motors, Brookline, Outback Flexline and a number of other specialist component suppliers.</p>
        <p>We can offer advice, helping you overcome your pumping problems, provide pumping and control solutions, supply replacement pumps and motors and provide complete ready to install mains and solar powered pumping kits, pre-assembled in my workshop.</p>
      </div>

      <h2 class="section-heading">Solar or mains powered?</h2>
      <p class="section-sub">If mains power is available the most cost effective solution may be a 230 volt or 3-phase powered pump.</p>

      <div class="copy">
        <p>In remote areas or locations where mains power is not available a solar powered pump system is very often the best solution. Solar powered pumps can be used to pump water from a water bore, a dam, a tank, creek or river. Solar powered pumps generally supply a few thousand litres per day right up the pumping volume required to operate a centre pivot irrigation system.</p>
        <p>The benefit of a solar powered system is the low installation cost compared to the cost of running mains power to a site, or purchasing and a running generator. The running and maintenance costs associated with a solar powered pump is low even compared to a windmill type pump.</p>
        <p><strong>We can design the pumping system and provide a free quote tailored to your application.</strong></p>
      </div>
    </div>

    <div class="media media--diagram" role="img" aria-label="Technical drawing of a solar bore pump system: PV panels, controller, float switch, water meter and submersible pump in the bore"></div>
    <div class="media media--truck" role="img" aria-label="Photo of a trailer loaded with pump gear on a dry paddock"></div>
    <div class="media media--bore" role="img" aria-label="Photo of a concrete bore head in a green yard"></div>
    <div class="media media--controller-small" role="img" aria-label="Photo of a pump controller box on a post"></div>

    <footer class="footer">
      <svg width="530" height="110" viewBox="0 0 530 110">
        <polyline points="40,54 300,54 322,76 530,76" fill="none" stroke="var(--blue-deep)" stroke-width="3"/>
        <polygon points="0,76 316,76 330,82 530,82 530,110 0,110" fill="var(--blue)"/>
        <polygon points="0,82 530,82 530,110 0,110" fill="var(--blue-deep)" opacity=".35"/>
      </svg>
      <p class="call-line">CALL 1300 555 018 OR MOBILE 0400 555 272</p>
      <p class="web-links"><span>www.sunwellflow.com.au</span><span>www.wellflowy.net.au</span><span>www.aquadeepflow.com.au</span></p>
    </footer>
  </section>

  <section class="page page--right">
    <svg class="header-bar" viewBox="0 0 530 40">
      <polygon points="198,6 530,6 530,40 222,40" fill="var(--grey)"/>
      <polygon points="0,0 192,0 216,26 0,26" fill="var(--blue-deep)"/>
      <polygon points="0,0 192,0 202,11 0,11" fill="var(--blue)" opacity=".45"/>
    </svg>
    <h1 class="header-title">Our Services</h1>

    <ul class="services">
      <li><svg viewBox="0 0 12 12"><path d="M1 6.5 4.5 10 11 2" fill="none" stroke="var(--blue)" stroke-width="2"/></svg>Submersible Pump Selection</li>
      <li><svg viewBox="0 0 12 12"><path d="M1 6.5 4.5 10 11 2" fill="none" stroke="var(--blue)" stroke-width="2"/></svg>Submersible Pump Shroud</li>
      <li><svg viewBox="0 0 12 12"><path d="M1 6.5 4.5 10 11 2" fill="none" stroke="var(--blue)" stroke-width="2"/></svg>Submersible Cable Splice</li>
      <li><svg viewBox="0 0 12 12"><path d="M1 6.5 4.5 10 11 2" fill="none" stroke="var(--blue)" stroke-width="2"/></svg>Solar Powered Submersible Pump Installation</li>
      <li><svg viewBox="0 0 12 12"><path d="M1 6.5 4.5 10 11 2" fill="none" stroke="var(--blue)" stroke-width="2"/></svg>Submersible Pump Installation</li>
      <li><svg viewBox="0 0 12 12"><path d="M1 6.5 4.5 10 11 2" fill="none" stroke="var(--blue)" stroke-width="2"/></svg>Solar Panel Installation</li>
      <li><svg viewBox="0 0 12 12"><path d="M1 6.5 4.5 10 11 2" fill="none" stroke="var(--blue)" stroke-width="2"/></svg>Torrentek GuardLine AUTO set-up</li>
    </ul>

    <div class="media media--shelves" role="img" aria-label="Photo of warehouse shelving stocked with pumps and parts"></div>
    <div class="media media--controller" role="img" aria-label="Photo of a solar pump controller mounted under a panel frame on red earth"></div>
    <div class="media media--panel" role="img" aria-label="Photo of a solar panel array in a fenced hillside paddock"></div>
    <div class="media media--drilling" role="img" aria-label="Photo of a drilling rig at work on a red dirt bore site"></div>

    <div class="copy owner-copy">
      <p><span class="lead">My name is Dean Marlow and I'm the owner of Sunwellflow.</span> I am seeking opportunities to grow my business by providing solar water bore pumping technology to users of traditional water bore pumping systems.</p>
      <p>Solar powered water bore pumps are perfect for land owners and managers who rely on water bores, without the ongoing power and maintenance costs. In many cases it is not possible to get a power supply to a new water bore or existing water source, making solar powered pumps the only practical and cost effective solution. Many windmill users are also upgrading their old windmills and replacing them with modern solar bore pump technologies.</p>
      <p>I have been involved in the drilling industry, pumps and associated equipment since the mid 1980's. I lead a team that have a range of recognised formal trades. We can help you with product selection and competitive pricing as well as complete do-it-yourself kits, installation, service and advice. I am happy to provide an obligation free quote and discuss options that best suit your requirements. You may be interested in a custom Sunwellflow Kit or other bore pumps and accessories. You can see what we do at www.sunwellflow.com.au. I'd be happy to chat to you about your requirements and help develop a custom solution for your property.</p>
    </div>

    <footer class="footer">
      <svg width="530" height="110" viewBox="0 0 530 110">
        <polygon points="0,50 150,50 172,30 530,30 530,34 174,34 152,54 0,54" fill="var(--blue-deep)"/>
        <polygon points="0,54 152,54 174,34 200,34 200,76 530,76 530,110 0,110" fill="var(--blue)"/>
        <polygon points="0,82 530,82 530,110 0,110" fill="var(--blue-deep)" opacity=".35"/>
      </svg>
      <p class="call-line">CALL 1300 555 018 OR MOBILE 0400 555 272</p>
      <p class="web-links"><span>www.sunwellflow.com.au</span><span>www.wellflowy.net.au</span><span>www.aquadeepflow.com.au</span></p>
    </footer>
  </section>
</main>
</body>
</html>
```